Tervolan Pty Ltd professional business card

A professional business card template using the colours from the supplied logo.
Clean crisp lines while, Modern while not being over the top.

Target Market(s)

Construction, commerical and industrial

Industry/Entity Type

Communications

Contact Information for Business Card

For a Communications, IT, Optical fibre installation company

Colors
37b8a4

```html
<!DOCTYPE html>
<html lang="en">
<head>
<meta charset="utf-8">
<title>Tervolan Pty Ltd – Business Card</title>
<link rel="stylesheet" href="https://fonts.googleapis.com/css2?family=Montserrat:wght@400;500;600&display=swap">
<style>
  :root {
    --bg: #d9dedf;
    --card: #f3f3f1;
    --teal: #2b9ba3;
    --ink: #5a5b5e;
    --ink-soft: #4a4b4e;
  }
  * { margin: 0; padding: 0; box-sizing: border-box; }
  html, body { width: 1200px; height: 852px; overflow: hidden; }
  body {
    background: var(--bg);
    font-family: "Montserrat", Arial, sans-serif;
    display: flex;
    align-items: center;
    justify-content: center;
    gap: 40px;
  }
  .card {
    width: 540px;
    height: 309px;
    background: var(--card);
    box-shadow: 0 6px 18px rgba(0,0,0,0.12);
    position: relative;
  }
  .brand {
    display: flex;
    align-items: center;
    gap: 12px;
    color: var(--ink);
    font-weight: 500;
    letter-spacing: 0.04em;
  }
  .brand-dot {
    width: 14px; height: 14px;
    border-radius: 50%;
    background: var(--teal);
  }
  /* Front */
  .card-front .brand {
    position: absolute;
    left: 38px;
    top: 128px;
    font-size: 34px;
  }
  .divider {
    position: absolute;
    left: 282px;
    top: 70px;
    width: 2px;
    height: 170px;
    background: var(--teal);
  }
  .details {
    position: absolute;
    left: 304px;
    top: 72px;
    color: var(--ink-soft);
    font-size: 14px;
    line-height: 1.5;
  }
  .details .name {
    color: var(--teal);
    font-weight: 600;
    font-size: 19px;
    letter-spacing: 0.05em;
    line-height: 1.2;
  }
  .details .role { margin-bottom: 6px; }
  .details .address { margin-bottom: 8px; }
  .contact { list-style: none; }
  .contact li { display: flex; align-items: center; gap: 8px; }
  .contact svg { width: 12px; height: 12px; flex: none; }
  .contact .accent { color: var(--teal); }
  /* Back */
  .card-back {
    display: flex;
    align-items: center;
    justify-content: center;
  }
  .card-back .brand { font-size: 48px; gap: 16px; }
  .card-back .brand-dot { width: 18px; height: 18px; }
</style>
</head>
<body>
  <section class="card card-front" aria-label="Business card front">
    <div class="brand"><span class="brand-dot"></span>TERVOLAN</div>
    <div class="divider"></div>
    <div class="details">
      <p class="name">MARTIN KESSLER</p>
      <p class="role">Director</p>
      <p class="address">1187 Larkfield Road<br>Corvallis, OR 97330</p>
      <ul class="contact">
        <li>
          <svg viewBox="0 0 12 12" aria-hidden="true"><path d="M3 1 L5 3.5 L4 5 Q5 7 7 8 L8.5 7 L11 9 L9.5 11 Q4 10.5 1 3 Z" fill="#2b9ba3"/></svg>
          (555) 014-2288
        </li>
        <li>
          <svg viewBox="0 0 12 12" aria-hidden="true"><rect x="1" y="2.5" width="10" height="7" fill="none" stroke="#2b9ba3" stroke-width="1.2"/><path d="M1 2.5 L6 6.5 L11 2.5" fill="none" stroke="#2b9ba3" stroke-width="1.2"/></svg>
          info@tervolan.com
        </li>
        <li>
          <svg viewBox="0 0 12 12" aria-hidden="true"><circle cx="6" cy="6" r="5" fill="none" stroke="#2b9ba3" stroke-width="1.1"/><ellipse cx="6" cy="6" rx="2.2" ry="5" fill="none" stroke="#2b9ba3" stroke-width="1"/><path d="M1 6 H11" stroke="#2b9ba3" stroke-width="1"/></svg>
          <span>www.<span class="accent">tervolan</span>.com</span>
        </li>
      </ul>
    </div>
  </section>

  <section class="card card-back" aria-label="Business card back">
    <div class="brand"><span class="brand-dot"></span>TERVOLAN</div>
  </section>
</body>
</html>
```